Bramble Hounds for dog food

its for dry dog food label that will be used for packaging. Two (2) labels for front and back.
In front it will have the brand of "Bramble Hounds" using graphics or pictures (photos) of Dogs, contain of wording super premium pet nutrition ; completed, balanced and quality nutrition ; hypo allergenic, grain free and spacing that can be switched among wording of 'chicken, beef, lamb, plus other variety.
on back it will have ingredients like common all dog food and having spaces that consist Protein..% ; Fat..% ; Fiber..% ; and moisture..% ; feeding suggestion that have standard suggestion for small breed to big dogs ; Also have US formula under licensed by ... ; net weight..kgs ; space for barcode and QR code
Updates
Target Market(s)
medium to high consumer
Colors
Designer to choose colors to be used in the design.
Requirements
Must have
- Completed, Balanced and Quality Nutrition, Hypo Allergenic
- "Chicken and Grain Free"
Nice to have
- the picture of puppy and adult dog (siberian husky)
- small and large Breed

```html
<!DOCTYPE html>
<html lang="en">
<head>
<meta charset="utf-8">
<title>Bramble Hounds – Large Breed Front Label</title>
<link rel="stylesheet" href="https://fonts.googleapis.com/css2?family=Libre+Baskerville:wght@400;700&family=EB+Garamond:wght@400;500&display=swap">
<style>
  :root {
    --brand-blue: #3372a3;
    --band-dark: #3a3a3c;
    --snow-light: #eef3f6;
    --snow-mid: #d7e2e8;
    --ink: #111111;
    --white: #ffffff;
    --burst-red: #e8232a;
    --burst-yellow: #f7e400;
  }
  html, body {
    margin: 0;
    padding: 0;
    width: 848px;
    height: 1200px;
    overflow: hidden;
    background: var(--white);
  }
  .label {
    position: relative;
    width: 848px;
    height: 1200px;
    overflow: hidden;
    background: var(--brand-blue);
    font-family: "Libre Baskerville", Georgia, serif;
  }
  .top-band { position: absolute; left: 0; top: 0; width: 100%; height: 152px; background: var(--brand-blue); }
  .top-stripe { position: absolute; left: 0; top: 152px; width: 100%; height: 23px; background: var(--band-dark); }
  .snow-scene {
    position: absolute; left: 0; top: 198px; width: 100%; height: 632px;
    background: linear-gradient(180deg, #f2f5f6 0%, #e4ecf0 30%, #dfe8ed 60%, #e8eef1 88%, var(--brand-blue) 100%);
  }
  .brand-mark { position: absolute; left: 0; top: 0; width: 100%; height: 600px; }
  .brand-dot {
    position: absolute; left: 665px; top: 228px; width: 120px; height: 120px;
    border-radius: 50%; background: var(--ink);
  }
  .brand-name {
    position: absolute; right: 91px; top: 310px; margin: 0;
    color: var(--brand-blue); font-weight: 700; text-align: right;
    line-height: 1;
  }
  .brand-name .word-1 { display: block; font-size: 160px; letter-spacing: -2px; }
  .brand-name .word-2 { display: block; font-size: 104px; margin-top: -6px; margin-right: 60px; }
  .tagline {
    position: absolute; left: 32px; top: 656px; margin: 0;
    font-size: 50px; font-weight: 700; line-height: 50px; color: var(--ink);
    text-shadow: 2px 2px 3px rgba(0,0,0,0.25);
  }
  .benefits {
    position: absolute; left: 39px; top: 866px; margin: 0;
    font-family: "EB Garamond", Georgia, serif; font-size: 38px; line-height: 42px;
    color: var(--white);
  }
  .flavour-band {
    position: absolute; left: 0; top: 1029px; width: 452px; height: 120px; background: var(--band-dark);
  }
  .flavour {
    position: absolute; left: 60px; top: 1043px; margin: 0;
    font-size: 45px; font-weight: 700; line-height: 49px; color: var(--white);
  }
  .dog-photo {
    position: absolute; left: 406px; top: 729px; width: 442px; height: 471px;
    background: radial-gradient(ellipse at 45% 40%, #6b6e73 0%, #4a4d52 40%, #8d8f93 75%, rgba(120,122,126,0.6) 100%);
    border-radius: 45% 40% 0 0;
  }
  .size-badge { position: absolute; left: 645px; top: 710px; width: 158px; height: 158px; }
  .size-badge text {
    font-family: "Libre Baskerville", Georgia, serif; font-weight: 700; font-size: 29px;
    fill: var(--burst-yellow); text-anchor: middle;
  }
</style>
</head>
<body>
<main class="label">
  <div class="top-band"></div>
  <div class="top-stripe"></div>

  <div class="snow-scene" role="img" aria-label="Photo of snowy ice field under a pale sky"></div>

  <div class="brand-mark">
    <span class="brand-dot"></span>
    <h1 class="brand-name"><span class="word-1">Bramble</span><span class="word-2">Hounds</span></h1>
  </div>

  <p class="tagline">Super Premium<br>Pet Nutrition</p>

  <p class="benefits">Completed, Balanced<br>and Quality Nutrition,<br>Hypo Allergenic</p>

  <div class="flavour-band"></div>
  <p class="flavour">Chicken and<br>Grain Free</p>

  <div class="dog-photo" role="img" aria-label="Photo of a sitting Siberian husky with blue eyes"></div>

  <svg class="size-badge" viewBox="-79 -79 158 158" aria-label="Large breed">
    <g fill="var(--burst-red)">
      <rect x="-55" y="-55" width="110" height="110"/>
      <rect x="-55" y="-55" width="110" height="110" transform="rotate(15)"/>
      <rect x="-55" y="-55" width="110" height="110" transform="rotate(30)"/>
      <rect x="-55" y="-55" width="110" height="110" transform="rotate(45)"/>
      <rect x="-55" y="-55" width="110" height="110" transform="rotate(60)"/>
      <rect x="-55" y="-55" width="110" height="110" transform="rotate(75)"/>
    </g>
    <g transform="rotate(-18)">
      <text x="0" y="-6">LARGE</text>
      <text x="0" y="26">BREED</text>
    </g>
  </svg>
</main>
</body>
</html>
```